Create 6 animated banners for makerting promotion

Create 6 animated banners similar to the example provided

Banner size needed

1 x 300x250
1 x 160x600
1 x 468x60
1 x 728x90
1 x 120x600
1 x 200x200

Text to be displayed:

intro screen: Trovaspark.com
animation > screen 1: The Most Refined Ad Serving Platform (pause 1.5 seconds)
animation > screen 2: Publishers - Get The Highest CPM Rates! (pause 1.5 seconds)
animation > screen 3: Advertisers - Get The Highest ROI! (pause 1.5 seconds)
animation > screen 4: Simple Dashboard (pause 1.5 seconds)
animation > screen 5: Profit From Top Quality Traffic (pause 1.5 seconds)
animation > screen 6: Account Managers Available To Help You Succeed (pause 1.5 seconds)
animation > screen 7: Click Here To Register (pause 1.5 seconds)
animation > screen 8: Trovaspark.com (pause 1.5 seconds)

background color: #0795d3

image provided must be animated gif

Attracted file with logo and sample banner
trovaspark.com logo font is Blender Pro Heavy

Target Market(s)

professional marketers, advertisers and publishers

Industry/Entity Type

Advertising

Font styles to use
Sans Serif

Requirements
Must have
• requirement text provided on description
• image must be animated gif
Nice to have
• slick animation
Should not have
• end image size should not be over 500kb

```html
<!DOCTYPE html>
<html lang="en">
<head>
<meta charset="utf-8">
<title>Trovaspark.com Banner Frames</title>
<link rel="stylesheet" href="https://fonts.googleapis.com/css2?family=Arimo:wght@400;700&display=swap">
<style>
  :root {
    --page-bg: #ffffff;
    --banner-blue: #0795d3;
    --banner-edge: #1a1a1a;
    --banner-text: #ffffff;
  }
  * { margin: 0; padding: 0; box-sizing: border-box; }
  html, body {
    width: 1200px;
    height: 1042px;
    overflow: hidden;
    background: var(--page-bg);
  }
  .frame-grid {
    position: relative;
    width: 1200px;
    height: 1042px;
    display: grid;
    grid-template-columns: repeat(3, 360px);
    grid-template-rows: repeat(3, 300px);
    column-gap: 24px;
    row-gap: 24px;
    padding: 42px 0 0 36px;
  }
  .banner {
    background: var(--banner-blue);
    border: 1px solid var(--banner-edge);
    display: flex;
    align-items: center;
    justify-content: center;
    color: var(--banner-text);
    font-family: "Arimo", Arial, sans-serif;
    text-transform: uppercase;
  }
  .banner-copy { text-align: left; line-height: 1; }
  .wordmark {
    font-weight: 700;
    font-size: 33px;
    letter-spacing: 0.5px;
  }
  .headline { font-size: 30px; line-height: 1.08; }
  .headline-large { font-size: 48px; line-height: 1; }
  .headline-medium { font-size: 42px; line-height: 1; }
  .headline-small { font-size: 27px; line-height: 1; }
  .subline { font-size: 19px; margin-top: 2px; }
  .subline-wide { font-size: 27px; margin-top: 2px; }
  .subline-tiny { font-size: 17px; margin-top: 3px; }
  .call-to-action {
    font-size: 26px;
    text-decoration: underline;
    text-underline-offset: 4px;
    text-decoration-thickness: 2px;
  }
</style>
</head>
<body>
  <main class="frame-grid">
    <section class="banner">
      <div class="banner-copy"><p class="wordmark">Trovaspark.com</p></div>
    </section>
    <section class="banner">
      <div class="banner-copy"><p class="headline">The Most Refined<br>Ad Serving Platform</p></div>
    </section>
    <section class="banner">
      <div class="banner-copy">
        <p class="headline-large">Publishers</p>
        <p class="subline">Get the highest CPM rates!</p>
      </div>
    </section>
    <section class="banner">
      <div class="banner-copy">
        <p class="headline-medium">Advertisers</p>
        <p class="subline-wide">Get the highest ROI!</p>
      </div>
    </section>
    <section class="banner">
      <div class="banner-copy"><p class="headline">Simple Dashboard</p></div>
    </section>
    <section class="banner">
      <div class="banner-copy">
        <p class="headline-medium">Profit From</p>
        <p class="subline-wide">Top Quality Traffic</p>
      </div>
    </section>
    <section class="banner">
      <div class="banner-copy">
        <p class="headline-small">Account Managers</p>
        <p class="subline-tiny">Available to help you succeed</p>
      </div>
    </section>
    <section class="banner">
      <div class="banner-copy"><p class="call-to-action">Click here to register</p></div>
    </section>
    <section class="banner">
      <div class="banner-copy"><p class="wordmark">Trovaspark.com</p></div>
    </section>
  </main>
</body>
</html>
```